User-interface and web design for new forum-style communication platform

We developed a new forum-style communication platform specially targetting stock investors to share and discuss information on companies listed on the stock exchange.

You have complete freedom for designing the user-interface and web design. Designs should include all features listed below.

Please read the attached document for full specifications. Also attached is a mockup of the layout, but this is only directional. A mockup for the user-profile is also attached, but does not need to be designed.

This project focusses on the homepage and thread view.

The winner(s) will be asked to design the complete project. (create thread box, user profile, registering, settings...)

We are looking for a well thought out, smart design that incorporates the specifications in the attached document. Please do not hesitate to contact us if anything is not clear.

Target Market(s)

Stock investors from 25 to 60 years old (the people that are currently on investor forums)

Industry/Entity Type

Communication

Font styles to use
Sans Serif

Colors

Designer to choose colors to be used in the design.

Requirements
Must have
• Full homepage design & Thread view specified in the attached document.
Nice to have
• Create thread view
- Field for adding tags
- field for subject of the thread
- text box with basic text editing
- method for sharing media
Should not have
• Logo design.

```html
<!DOCTYPE html>
<html lang="en">
<head>
<meta charset="utf-8">
<title>#northwind – Conversations</title>
<link href="https://fonts.googleapis.com/css2?family=Open+Sans:wght@400;600&family=Ubuntu:wght@400;500&display=swap" rel="stylesheet">
<style>
:root{
  --page:#efefef;
  --header:#2c3136;
  --header-line:#22272b;
  --white:#fff;
  --card:#f5f5f5;
  --border:#dcdcdc;
  --text:#222;
  --muted:#8a8a8a;
  --light:#a9a9a9;
  --link:#5fa8c9;
  --accent:#f2b22a;
  --send:#4a90ad;
}
*{box-sizing:border-box;margin:0;padding:0}
html,body{width:1029px;height:1200px;overflow:hidden}
body{background:var(--page);font-family:"Open Sans",sans-serif;color:var(--text);position:relative}
.topbar{position:absolute;left:0;top:0;width:1029px;height:59px;background:linear-gradient(#363c42,#262b30);border-bottom:1px solid var(--header-line)}
.menu-btn{position:absolute;left:0;top:0;width:93px;height:59px;border-right:1px solid #1e2226;display:flex;align-items:center;justify-content:center}
.brand{position:absolute;left:111px;top:15px;color:#fff;font-family:"Ubuntu",sans-serif;font-size:20px}
.search{position:absolute;left:205px;top:17px;width:342px;height:27px;background:#fff;border-radius:2px;display:flex;align-items:center;padding-left:9px}
.notify{position:absolute;left:753px;top:0;width:65px;height:59px;border-left:1px solid #1e2226;border-right:1px solid #1e2226;display:flex;align-items:center;justify-content:center}
.badge{position:absolute;left:39px;top:12px;width:16px;height:16px;border-radius:50%;background:var(--accent);color:#fff;font-size:8px;font-weight:600;display:flex;align-items:center;justify-content:center}
.user{position:absolute;left:832px;top:15px;display:flex;gap:8px;align-items:center}
.user .avatar{width:29px;height:29px;background:linear-gradient(#8a7a6a,#4e4640);border:1px solid #666}
.user .name{color:#fff;font-family:"Ubuntu",sans-serif;font-size:11px;font-weight:500}
.user .mail{color:var(--link);font-size:9px;margin-top:2px}
.user svg{margin-left:6px;margin-top:6px}
.page-title{position:absolute;left:208px;top:95px;display:flex;align-items:center;gap:6px;font-family:"Ubuntu",sans-serif}
.page-title h1{font-size:19px;font-weight:400;color:var(--text)}
.crumbs{margin-left:20px;font-size:14px;color:#8c8c8c;display:flex;gap:8px}
.crumbs span.sep{color:#bbb}
.sidenav{position:absolute;left:43px;top:126px;width:138px;background:#fff;border:1px solid var(--border);box-shadow:0 1px 1px #c8c8c8;font-family:"Ubuntu",sans-serif}
.sidenav .main{height:31px;display:flex;align-items:center;gap:10px;padding-left:12px;font-size:14px;color:#6a6a6a;border-bottom:1px solid var(--border)}
.sidenav .main.active{background:#eef3f6}
.sidenav .sub{height:30px;display:flex;align-items:center;justify-content:space-between;padding:0 14px 0 42px;font-family:"Open Sans",sans-serif;font-size:11px;color:#777;background:#f7f7f7;border-bottom:1px solid var(--border)}
.sidenav .sub:last-child{border-bottom:none}
.panel{position:absolute;left:204px;top:126px;width:781px;height:1008px;background:#fff;border:1px solid var(--border);border-radius:3px;box-shadow:0 1px 2px #c8c8c8;padding:31px 24px 0 31px}
.post{height:241px;display:flex;gap:26px;position:relative}
.post .face{width:30px;height:30px;flex:none;background:linear-gradient(#d59a6e,#8c5a3c);border:1px solid #bbb;box-shadow:0 1px 1px #aaa}
.post .body{width:670px}
.card{height:114px;background:var(--card);border:1px solid #e6e6e6;border-bottom:2px solid #cfcfcf;border-radius:3px;padding:17px 12px 0;position:relative}
.card::before{content:"";position:absolute;left:-7px;top:20px;border:7px solid transparent;border-left:0;border-right-color:#eee}
.card h2{font-family:"Ubuntu",sans-serif;font-weight:400;font-size:14px;display:flex;align-items:baseline;gap:8px}
.card h2 small{font-family:"Open Sans",sans-serif;font-size:7px;color:#777}
.card p{margin-top:6px;font-size:8.6px;line-height:14.5px;color:#888}
.meta{display:flex;justify-content:space-between;margin-top:8px;font-size:9.5px;color:var(--light)}
.meta .left{display:flex;gap:9px}
.meta .right{display:flex;gap:22px}
.meta .right span{display:flex;align-items:center;gap:4px}
.reply-form{display:flex;gap:7px;margin-top:12px}
.reply-form .field{width:614px;height:25px;border:1px solid #ccc;border-radius:2px;font-size:11px;color:#777;padding:5px 9px}
.reply-form .send{width:49px;height:25px;background:linear-gradient(#5ca3c0,var(--send));border-radius:2px;color:#fff;font-size:11px;display:flex;align-items:center;justify-content:center}
.divider{position:absolute;left:2px;right:0;top:203px;height:4px;border-top:1px dotted #bbb;border-bottom:1px dotted #bbb}
</style>
</head>
<body>
<header class="topbar">
  <div class="menu-btn"><svg width="13" height="11"><rect y="0" width="13" height="2" fill="#fff"/><rect y="4.5" width="13" height="2" fill="#fff"/><rect y="9" width="13" height="2" fill="#fff"/></svg></div>
  <div class="brand">Logo</div>
  <div class="search"><svg width="9" height="9"><circle cx="5.5" cy="3.5" r="2.6" stroke="#222" stroke-width="1.5" fill="none"/><line x1="3.5" y1="5.5" x2="0.8" y2="8.2" stroke="#222" stroke-width="1.8"/></svg></div>
  <div class="notify">
    <svg width="14" height="14"><circle cx="6" cy="4" r="3" fill="#fff"/><path d="M0 13c0-4 3-5 6-5s6 1 6 5z" fill="#fff"/></svg>
    <span class="badge">10</span>
  </div>
  <div class="user">
    <div class="avatar" role="img" aria-label="User profile photo"></div>
    <div><div class="name">Sam Rivera</div><div class="mail">sam.rivera@example.com</div></div>
    <svg width="8" height="5"><path d="M1 1l3 3 3-3" stroke="#fff" stroke-width="1.5" fill="none"/></svg>
  </div>
</header>

<div class="page-title">
  <svg width="14" height="12"><ellipse cx="8" cy="5" rx="6" ry="4.5" fill="#222"/><path d="M3 8l-2 4 5-3z" fill="#222"/></svg>
  <h1>#northwind</h1>
  <nav class="crumbs"><span>Home</span><span class="sep">/</span><span>Conversations</span><span class="sep">/</span><span>Public</span><span class="sep">/</span><span>#northwind</span></nav>
</div>

<aside class="sidenav">
  <div class="main active"><svg width="14" height="12"><path d="M7 0l7 6h-2v6H9V8H5v4H2V6H0z" fill="var(--accent)"/></svg>Home</div>
  <div class="main"><svg width="16" height="12"><ellipse cx="6" cy="5" rx="6" ry="4.5" fill="#ccc"/><ellipse cx="11" cy="7" rx="5" ry="4" fill="#ddd"/></svg>Topics</div>
  <div class="sub">Public<svg width="4" height="7"><path d="M0 0l4 3.5L0 7z" fill="#777"/></svg></div>
  <div class="sub">Following<svg width="4" height="7"><path d="M0 0l4 3.5L0 7z" fill="#777"/></svg></div>
  <div class="sub">Contacts<svg width="4" height="7"><path d="M0 0l4 3.5L0 7z" fill="#777"/></svg></div>
</aside>

<main class="panel">
  <article class="post">
    <div class="face" role="img" aria-label="Author profile photo"></div>
    <div class="body">
      <div class="card"><h2>What do you think of Nimbus OS 8? <small>Posted by Sam Rivera &nbsp;| &nbsp;May 27, 2013 / 09:32 am</small></h2>
      <p>It is a long established fact that a reader will be distracted by the readable content of a page when looking at its layout. The point of using Lorem Ipsum is that it has a more-or-less normal distribution of letters, as opposed to using 'Content here, content here', making it look like readable Eng-lish. Lorem ipsum dolor sit amet, consectetur adipisicing elit, sed do eiusmod tempor incididunt ut labore et dolore magna aliqua. Ut enim ad minim veniam, quis nostrud exercitation ullamco laboris nisi ut aliquip ex ea commodo consequat.</p></div>
      <div class="meta"><div class="left"><span>Read More</span><span>|</span><span>12 replies</span><span>|</span><span>25 comments</span></div>
      <div class="right"><span>◌ Reply</span><span>↗ Share</span><span>♡ Favorite</span></div></div>
      <div class="reply-form"><div class="field">Enter your message ...</div><div class="send">Send</div></div>
    </div>
    <div class="divider"></div>
  </article>
  <article class="post">
    <div class="face" role="img" aria-label="Author profile photo"></div>
    <div class="body">
      <div class="card"><h2>What do you think of Nimbus OS 8? <small>Posted by Sam Rivera &nbsp;| &nbsp;May 27, 2013 / 09:32 am</small></h2>
      <p>It is a long established fact that a reader will be distracted by the readable content of a page when looking at its layout. The point of using Lorem Ipsum is that it has a more-or-less normal distribution of letters, as opposed to using 'Content here, content here', making it look like readable Eng-lish. Lorem ipsum dolor sit amet, consectetur adipisicing elit, sed do eiusmod tempor incididunt ut labore et dolore magna aliqua. Ut enim ad minim veniam, quis nostrud exercitation ullamco laboris nisi ut aliquip ex ea commodo consequat.</p></div>
      <div class="meta"><div class="left"><span>Read More</span><span>|</span><span>12 replies</span><span>|</span><span>25 comments</span></div>
      <div class="right"><span>◌ Reply</span><span>↗ Share</span><span>♡ Favorite</span></div></div>
      <div class="reply-form"><div class="field">Enter your message ...</div><div class="send">Send</div></div>
    </div>
    <div class="divider"></div>
  </article>
  <article class="post">
    <div class="face" role="img" aria-label="Author profile photo"></div>
    <div class="body">
      <div class="card"><h2>What do you think of Nimbus OS 8? <small>Posted by Sam Rivera &nbsp;| &nbsp;May 27, 2013 / 09:32 am</small></h2>
      <p>It is a long established fact that a reader will be distracted by the readable content of a page when looking at its layout. The point of using Lorem Ipsum is that it has a more-or-less normal distribution of letters, as opposed to using 'Content here, content here', making it look like readable Eng-lish. Lorem ipsum dolor sit amet, consectetur adipisicing elit, sed do eiusmod tempor incididunt ut labore et dolore magna aliqua. Ut enim ad minim veniam, quis nostrud exercitation ullamco laboris nisi ut aliquip ex ea commodo consequat.</p></div>
      <div class="meta"><div class="left"><span>Read More</span><span>|</span><span>12 replies</span><span>|</span><span>25 comments</span></div>
      <div class="right"><span>◌ Reply</span><span>↗ Share</span><span>♡ Favorite</span></div></div>
      <div class="reply-form"><div class="field">Enter your message ...</div><div class="send">Send</div></div>
    </div>
    <div class="divider"></div>
  </article>
  <article class="post">
    <div class="face" role="img" aria-label="Author profile photo"></div>
    <div class="body">
      <div class="card"><h2>What do you think of Nimbus OS 8? <small>Posted by Sam Rivera &nbsp;| &nbsp;May 27, 2013 / 09:32 am</small></h2>
      <p>It is a long established fact that a reader will be distracted by the readable content of a page when looking at its layout. The point of using Lorem Ipsum is that it has a more-or-less normal distribution of letters, as opposed to using 'Content here, content here', making it look like readable Eng-lish. Lorem ipsum dolor sit amet, consectetur adipisicing elit, sed do eiusmod tempor incididunt ut labore et dolore magna aliqua. Ut enim ad minim veniam, quis nostrud exercitation ullamco laboris nisi ut aliquip ex ea commodo consequat.</p></div>
      <div class="meta"><div class="left"><span>Read More</span><span>|</span><span>12 replies</span><span>|</span><span>25 comments</span></div>
      <div class="right"><span>◌ Reply</span><span>↗ Share</span><span>♡ Favorite</span></div></div>
      <div class="reply-form"><div class="field">Enter your message ...</div><div class="send">Send</div></div>
    </div>
    <div class="divider"></div>
  </article>
</main>
</body>
</html>
```